Venlow Vaults -responsive, bootstrap website design

Looking to build a responsive service website.

Logo and pictures have been provided.

PLEASE REVIEW ATTACHED DESIGN STYLE GUIDES & CLIENT CREATIVE BRIEF FOR OUR REQUIREMENT. THANK YOU AND GOOD LUCK!
Updates

Industry/Entity Type

Build

```html
<!DOCTYPE html>
<html lang="en">
<head>
<meta charset="utf-8">
<title>Venlow Vaults</title>
<link rel="stylesheet" href="https://fonts.googleapis.com/css2?family=Mulish:ital,wght@0,400;0,600;0,700;1,400&family=Open+Sans:wght@400;600&family=Ubuntu:wght@500&family=Roboto:wght@300;400&display=swap">
<style>
:root{
  --paper:#eeebe3;
  --white:#ffffff;
  --ink:#222222;
  --text:#666666;
  --muted:#8a8a8a;
  --nav:#111111;
  --nav-active:#454545;
  --wine:#8e2a2c;
  --orange:#e0603a;
  --green:#3f8a2a;
  --wood:#ead7b3;
  --panel:#f6f5f2;
  --link:#2a64c8;
}
*{margin:0;padding:0;box-sizing:border-box}
html,body{width:990px;height:1200px;overflow:hidden}
body{background:var(--paper);font-family:"Mulish",Arial,sans-serif;color:var(--text);position:relative}
.abs{position:absolute}
.page{position:absolute;left:91px;top:40px;width:808px;height:1160px;background:var(--white)}
.logo{left:106px;top:64px;width:122px;height:93px;border:1px solid #555;border-radius:8px;display:flex;align-items:center;justify-content:center;font-family:"Mulish",sans-serif;font-weight:700;font-size:17px;color:var(--ink);text-align:center;line-height:1.15}
.contact{right:331px;top:61px;text-align:right}
.contact .welcome{font-family:"Roboto",sans-serif;font-size:11px;color:var(--orange)}
.contact .phone{font-family:"Roboto",sans-serif;font-weight:300;font-size:20px;color:var(--ink);margin-top:3px;display:flex;align-items:center;gap:6px;justify-content:flex-end}
.contact .hours{font-family:"Roboto",sans-serif;font-size:10px;color:var(--muted);margin-top:1px}
.currency{left:728px;top:63px;font-family:"Open Sans",sans-serif;font-size:9.5px;color:#333;display:flex;align-items:center;gap:5px}
.currency .select{width:70px;height:16px;border:1px solid #ccc;color:#d9a25a;font-size:9px;padding-left:3px;line-height:14px;position:relative}
.currency .select::after{content:"";position:absolute;right:1px;top:1px;width:12px;height:12px;border:1px solid #888;background:#eee}
.login{right:99px;top:100px;font-family:"Open Sans",sans-serif;font-size:9.5px;color:var(--wine)}
.hr-top{left:710px;top:119px;width:183px;height:1px;background:#e6c79b}
.cart-pic{left:738px;top:127px;width:54px;height:40px;border-radius:4px;background:linear-gradient(135deg,#e4b870,#e9c86a 50%,#e08a5a)}
.cart-text{left:807px;top:134px;font-family:"Open Sans",sans-serif}
.cart-text .t{font-size:11.5px;color:var(--orange);letter-spacing:-.2px}
.cart-text .n{font-size:9.5px;color:#7aa23a;font-weight:600}
.nav{left:91px;top:190px;width:808px;height:38px;background:var(--nav)}
.nav a{position:absolute;top:0;height:38px;line-height:38px;font-family:"Open Sans",sans-serif;font-weight:600;font-size:12.3px;color:#fff;text-decoration:none}
.nav a.active{background:var(--nav-active);padding:0 0 0 19px;width:75px;font-weight:400}
.hero{left:99px;top:236px;width:793px;height:304px;background:linear-gradient(100deg,#ece7df 0%,#d9dde2 35%,#b9cbe0 55%,#7f9a5a 80%,#4f6e2c 100%);border:1px solid #ddd}
.hero-card{left:128px;top:278px;width:284px;height:218px;background:#171717;box-shadow:2px 2px 5px rgba(0,0,0,.4)}
.hero-card .frame{position:absolute;inset:8px;border:1px solid #ddd;outline:1px solid #ddd;outline-offset:-4px}
.hero-card h1{position:absolute;left:25px;top:36px;font-family:"Mulish",sans-serif;font-weight:700;font-size:26px;color:#fff;letter-spacing:.2px}
.hero-card p{position:absolute;left:29px;top:79px;width:210px;font-size:11.5px;line-height:14.4px;color:#fff}
.shop-btn{position:absolute;left:29px;top:154px;width:99px;height:28px;border-radius:14px;background:var(--wine);color:#fff;font-size:10px;line-height:28px;text-align:center;letter-spacing:.2px}
.intro h2{position:absolute;left:99px;top:563px;font-family:"Mulish",sans-serif;font-weight:600;font-size:23px;color:var(--ink);letter-spacing:-.3px}
.intro p{position:absolute;left:99px;width:535px;font-size:10.4px;line-height:16.5px;color:var(--text)}
.intro-pic{left:675px;top:558px;width:214px;height:162px;background:linear-gradient(120deg,#fff 0%,#e9e7b0 35%,#b6c24e 55%,#5a4a2e 80%,#7aa04a 100%)}
.products-line{left:91px;top:746px;width:808px;height:1px;background:#eee}
.card{position:absolute;top:747px;height:228px}
.card .sep{position:absolute;right:0;top:0;width:1px;height:228px;background:linear-gradient(#f6f6f6,#eee,#f6f6f6)}
.bottle{position:absolute;top:16px;width:70px;height:116px;background:linear-gradient(160deg,#3a3a3a,#1a1a1a 60%,#4a2020)}
.price{position:absolute;top:138px;font-family:"Roboto",sans-serif;font-size:15.5px;color:var(--ink)}
.price.old{text-decoration:line-through}
.desc{position:absolute;top:160px;font-size:9px;color:var(--muted);white-space:nowrap}
.cart-btn{position:absolute;top:181px;width:31px;height:30px;background:#222;border:1px solid #000;display:flex;align-items:center;justify-content:center}
.qv-btn{position:absolute;top:181px;width:95px;height:30px;background:#222;border:1px solid #000;border-radius:3px;color:#fff;font-family:"Roboto",sans-serif;font-size:14px;line-height:28px;text-align:center}
.qv-btn.hot{background:var(--wine);border-color:#5a1414}
.wood{left:91px;top:1005px;width:808px;height:152px;background:repeating-linear-gradient(90deg,var(--wood) 0 30px,#e3cda6 30px 32px,#eddcbc 32px 70px)}
.panel{left:107px;top:1023px;width:776px;height:118px;background:var(--panel)}
.news h3{position:absolute;top:1041px;font-family:"Ubuntu",sans-serif;font-weight:500;font-size:16.5px;color:#333}
.news p{position:absolute;top:1068px;width:275px;font-size:10px;line-height:15px;color:#777}
.news .date{position:absolute;top:1103px;font-style:italic;font-size:10px;color:#8ba05a}
.news .more{position:absolute;top:1103px;font-size:10px;color:var(--link);text-decoration:underline}
.badge{position:absolute;background:#cfcfcf;border-radius:3px}
.pin{position:absolute;top:1005px;width:1px;height:26px;background:#555}
.pin::after{content:"";position:absolute;left:-3px;bottom:-3px;width:7px;height:7px;border-radius:50%;background:#333}
.copyright{left:91px;top:1172px;width:808px;text-align:center;font-size:10px;color:#555}
</style>
</head>
<body>
<div class="page"></div>

<header>
  <div class="abs logo">Venlow<br>Vaults</div>
  <div class="abs contact">
    <div class="welcome">Welcome to our online store!</div>
    <div class="phone">
      <svg width="16" height="16" viewBox="0 0 24 24"><path fill="#4c9a2a" d="M6.6 10.8c1.4 2.8 3.8 5.1 6.6 6.6l2.2-2.2c.3-.3.7-.4 1-.2 1.1.4 2.3.6 3.6.6.6 0 1 .4 1 1V20c0 .6-.4 1-1 1C10.6 21 3 13.4 3 4c0-.6.4-1 1-1h3.5c.6 0 1 .4 1 1 0 1.3.2 2.5.6 3.6.1.3 0 .7-.2 1z"/></svg>
      1(800) 555-0142
    </div>
    <div class="hours">Hours: 8am-4pm PST M-Fri</div>
  </div>
  <div class="abs currency">Currencies:
    <span class="select">US Dollar</span>
    <svg width="29" height="15" viewBox="0 0 29 15"><rect width="29" height="15" fill="#1f3a8a"/><path d="M0 0L29 15M29 0L0 15" stroke="#fff" stroke-width="3"/><path d="M0 0L29 15M29 0L0 15" stroke="#c8102e" stroke-width="1"/><rect x="11.5" width="6" height="15" fill="#fff"/><rect y="5" width="29" height="5" fill="#fff"/><rect x="13" width="3" height="15" fill="#c8102e"/><rect y="6" width="29" height="3" fill="#c8102e"/></svg>
  </div>
  <div class="abs login">Log In</div>
  <div class="abs hr-top"></div>
  <div class="abs cart-pic" role="img" aria-label="Wicker basket full of fruit"></div>
  <div class="abs cart-text"><div class="t">SHOPPING CART</div><div class="n">0 items</div></div>
</header>

<nav class="abs nav">
  <a class="active" style="left:6px" href="#">HOME</a>
  <a style="left:96px" href="#">About Us</a>
  <a style="left:183px" href="#">Our Hampers</a>
  <a style="left:294px" href="#">Corporate Gifts</a>
  <a style="left:416px" href="#">Subscriptions</a>
  <a style="left:528px" href="#">Our Story</a>
  <a style="left:617px" href="#">Delivery Info</a>
  <a style="left:723px" href="#">Contact Us</a>
</nav>

<section>
  <div class="abs hero" role="img" aria-label="Glasses of red wine, picnic basket, grapes and cheese in a vineyard"></div>
  <div class="abs hero-card">
    <div class="frame"></div>
    <h1>Venlow Vaults</h1>
    <p>It is a long established fact that a reader will be distracted by the readable content of a page when looking at its layout.</p>
    <div class="shop-btn">SHOP NOW &nbsp;▸</div>
  </div>
</section>

<section class="intro">
  <h2>Welcome To Venlow Vaults</h2>
  <p style="top:597px">Lorem ipsum dolor sit amet, consectetur adipisicing elit, sed do eiusmod tempor incididunt ut labore et dolore magna aliqua. Ut enim ad minim veniam, quis nostrud exercitation ullamco laboris nisi ut aliquip ex ea commodo consequat.</p>
  <p style="top:658px">Duis aute irure dolor in reprehenderit in voluptate velit esse cillum dolore eu fugiat nulla pariatur. Excepteur sint occaecat cupidatat non proident, sunt in culpa qui officia deserunt mollit anim id est laborum. Ut enim ad minim veniam, quis nostrud exercitation ullamco laboris nisi ut aliquip ex ea commodo consequat.</p>
  <div class="abs intro-pic" role="img" aria-label="Glass of white wine with green grapes on a barrel and vine leaves"></div>
</section>

<section class="products">
  <div class="abs products-line"></div>

  <div class="card" style="left:91px;width:196px"><div class="sep"></div>
    <div class="bottle" style="left:69px" role="img" aria-label="Two bottles of red wine"></div>
    <div class="price old" style="left:18px">$ 25.00</div><div class="price" style="left:112px">$ 15.00</div>
    <div class="desc" style="left:18px">Contrairement à une opinion répa.</div>
    <div class="cart-btn" style="left:19px"><svg width="16" height="14" viewBox="0 0 16 14"><path d="M1 1h3l2 7h7l2-5H5" fill="none" stroke="#fff" stroke-width="1.8"/><circle cx="7" cy="12" r="1.3" fill="#fff"/><circle cx="12" cy="12" r="1.3" fill="#fff"/></svg></div>
    <div class="qv-btn" style="left:58px">Quick View</div>
  </div>

  <div class="card" style="left:300px;width:196px"><div class="sep"></div>
    <div class="bottle" style="left:69px" role="img" aria-label="Two bottles of red wine"></div>
    <div class="price old" style="left:18px">$ 25.00</div><div class="price" style="left:112px">$ 15.00</div>
    <div class="desc" style="left:18px">Contrairement à une opinion répa.</div>
    <div class="cart-btn" style="left:19px"><svg width="16" height="14" viewBox="0 0 16 14"><path d="M1 1h3l2 7h7l2-5H5" fill="none" stroke="#fff" stroke-width="1.8"/><circle cx="7" cy="12" r="1.3" fill="#fff"/><circle cx="12" cy="12" r="1.3" fill="#fff"/></svg></div>
    <div class="qv-btn" style="left:58px">Quick View</div>
  </div>

  <div class="card" style="left:497px;width:206px"><div class="sep"></div>
    <div class="bottle" style="left:72px" role="img" aria-label="Two bottles of red wine"></div>
    <div class="price old" style="left:18px">$ 25.00</div><div class="price" style="left:112px">$ 15.00</div>
    <div class="desc" style="left:18px">Contrairement à une opinion répa.</div>
    <div class="cart-btn" style="left:19px"><svg width="16" height="14" viewBox="0 0 16 14"><path d="M1 1h3l2 7h7l2-5H5" fill="none" stroke="#fff" stroke-width="1.8"/><circle cx="7" cy="12" r="1.3" fill="#fff"/><circle cx="12" cy="12" r="1.3" fill="#fff"/></svg></div>
    <div class="qv-btn" style="left:58px">Quick View</div>
  </div>

  <div class="card" style="left:709px;width:190px">
    <div class="bottle" style="left:66px" role="img" aria-label="Two bottles of red wine"></div>
    <div class="price old" style="left:18px">$ 25.00</div><div class="price" style="left:112px">$ 15.00</div>
    <div class="desc" style="left:18px">Contrairement à une opinion répa.</div>
    <div class="cart-btn" style="left:19px"><svg width="16" height="14" viewBox="0 0 16 14"><path d="M1 1h3l2 7h7l2-5H5" fill="none" stroke="#fff" stroke-width="1.8"/><circle cx="7" cy="12" r="1.3" fill="#fff"/><circle cx="12" cy="12" r="1.3" fill="#fff"/></svg></div>
    <div class="qv-btn hot" style="left:58px">Quick View</div>
  </div>
</section>

<footer>
  <div class="abs wood"></div>
  <div class="pin" style="left:122px"></div>
  <div class="pin" style="left:868px"></div>
  <div class="abs panel"></div>
  <div class="news">
    <h3 style="left:147px">Typi non habent</h3>
    <p style="left:147px">Pocessus dynamicus, qui sequitur mutationem consuetui lectorum. Mirum est notare quam littera gothica, quam</p>
    <div class="date" style="left:147px">14 Mar, 2014</div>
    <div class="more" style="left:370px">More info</div>

    <h3 style="left:445px">Anteposuerit</h3>
    <p style="left:445px">Sus dynamicus, qui sequitur mutationem consuetuium lectorum. Mirum est notare quam littera gothica unc</p>
    <div class="date" style="left:445px">14 Mar, 2014</div>
    <div class="more" style="left:669px">More info</div>
  </div>
  <div class="badge" style="left:720px;top:1066px;width:80px;height:18px"></div>
  <div class="badge" style="left:808px;top:1066px;width:62px;height:20px"></div>
  <div class="badge" style="left:756px;top:1096px;width:112px;height:14px"></div>
  <div class="abs copyright">Copyright © 2014 Venlow Vaults</div>
</footer>
</body>
</html>
```